"Breathe & Bloom" Book Cover 5.5x8.5

Title of the book is "Breathe & Bloom"
Subtitle is "Unmasking Pricing Myths"
I've used PixelGuild on multiple occasions you can look on my Borvex page, Mark Delwitt, to see the covers I've used in the other projects I've done.
The target audience are people who have been tricked to think they can't retire because inflation, i.e. cost of living is going up so much they must work to keep up. There is no evidence of this.
And those are the people I want to reach so they can "Breathe...and Bloom."
Target Market(s)
Americans aged 55 and over who are thinking about retirement
Industry/Entity Type
Financial
Requirements
Nice to have
- Keep It Simple, Stupid is my mantra. Just make it pop out when people are browsing
Should not have
- No piggy banks. No old people sitting on a beach.

```html
<!DOCTYPE html>
<html lang="en">
<head>
<meta charset="utf-8">
<title>Breathe &amp; Bloom — Book Cover</title>
<link rel="stylesheet" href="https://fonts.googleapis.com/css2?family=Cinzel+Decorative:wght@700&family=Cinzel:wght@400&family=Jost:wght@600&display=swap">
<style>
  :root {
    --night: #0b0a0c;
    --gold: #e3c47f;
    --sky-teal: #55b9d1;
    --sub-teal: #0f5f6c;
    --band: #94bfcd;
    --ink: #111214;
    --photo-light: #8fc0d3;
    --photo-mid: #6f8f96;
    --photo-dark: #3e3431;
  }
  html, body {
    margin: 0;
    padding: 0;
    overflow: hidden;
    background: var(--night);
  }
  .cover {
    position: relative;
    width: 800px;
    height: 1200px;
    overflow: hidden;
    background: var(--night);
  }
  .cover-photo {
    position: absolute;
    left: 0;
    top: 491px;
    width: 800px;
    height: 568px;
    background: linear-gradient(to bottom,
      var(--photo-light) 0%,
      var(--photo-mid) 60%,
      var(--photo-dark) 100%);
  }
  .cover-art {
    position: absolute;
    inset: 0;
    width: 800px;
    height: 1200px;
  }
  .title-line {
    font-family: "Cinzel Decorative", "Cinzel", serif;
    font-weight: 700;
  }
  .title-main { fill: var(--gold); }
  .title-second { fill: var(--sky-teal); }
  .subtitle {
    font-family: "Jost", "Futura", sans-serif;
    font-weight: 600;
    font-size: 32px;
    letter-spacing: 1.5px;
    fill: var(--sub-teal);
  }
  .author-band { fill: var(--band); }
  .author {
    font-family: "Cinzel", serif;
    font-weight: 400;
    fill: var(--ink);
  }
</style>
</head>
<body>
  <div class="cover">
    <div class="cover-photo" role="img" aria-label="Photo of a bright empty room with tall windows looking out over the ocean, dunes and a polished wooden floor"></div>

    <svg class="cover-art" viewBox="0 0 800 1200" xmlns="http://www.w3.org/2000/svg">
      <defs>
        <filter id="lift" x="-5%" y="-5%" width="110%" height="120%">
          <feDropShadow dx="0" dy="4" stdDeviation="4" flood-color="#000" flood-opacity="0.6"/>
        </filter>
      </defs>

      <text class="title-line title-main" x="38" y="306" font-size="250" textLength="742" lengthAdjust="spacingAndGlyphs" filter="url(#lift)">BREATHE</text>

      <text class="title-line title-second" x="168" y="510" font-size="178" textLength="612" lengthAdjust="spacingAndGlyphs" filter="url(#lift)">&amp; BLOOM</text>

      <g class="subtitle" text-anchor="middle">
        <text x="342" y="579">UNMASKING</text>
        <text x="342" y="619">PRICING</text>
        <text x="342" y="658">MYTHS</text>
      </g>

      <rect class="author-band" x="0" y="1059" width="800" height="141"/>
      <text class="author" x="405" y="1168" text-anchor="middle" font-size="108" textLength="600" lengthAdjust="spacingAndGlyphs">MARK DELWITT</text>
    </svg>
  </div>
</body>
</html>
```